BPR Business Card

We need a business card that reflect our business, we have put anther business card as an example of what we like but please feel free to do your own thing.

Here are the items to be placed on card

Glen Harwick
Bright Parcel Route
Mobile: 917-555-4862
Office: 516-555-7104
Fax: 866-555-3927
Email: info@brightparcelroute.example
Website: brightparcelroute.example

I have added raw files to upload

Glen Harwick
Bright Parcel Route
Mobile: 917-555-4862
Office: 516-555-7104
Fax: 866-555-3927 

Target Market(s)

Natural product manufactures, and retailers and distributors

Industry/Entity Type

Business

Requirements
Must have
• 1. Logo
2. The colors of the company

```html
<!DOCTYPE html>
<html lang="en">
<head>
<meta charset="utf-8">
<title>Bright Parcel Route – Business Card</title>
<link rel="stylesheet" href="https://fonts.googleapis.com/css2?family=Arimo:wght@400;700&display=swap">
<style>
  :root {
    --brand-green: #6bb81e;
    --ink-black: #000000;
    --card-white: #ffffff;
    --backdrop: #d9d9d9;
    --text-light: #ffffff;
  }
  * { margin: 0; padding: 0; box-sizing: border-box; }
  html, body {
    width: 1200px; height: 900px; overflow: hidden;
    background: var(--backdrop);
    font-family: "Arimo", Arial, sans-serif;
  }
  .canvas { position: relative; width: 1200px; height: 900px; }

  .card {
    position: absolute; width: 640px; height: 365px;
    background: var(--card-white);
    box-shadow: 0 10px 24px rgba(0,0,0,0.35);
    overflow: hidden;
  }
  .card--contact { left: 280px; top: 60px; }
  .card--brand { left: 280px; top: 475px; }

  /* contact side */
  .contact-band {
    position: absolute; left: 0; right: 0; top: 158px; bottom: 0;
    background: var(--ink-black);
  }
  .edge-strip { position: absolute; width: 12px; }
  .card--contact .edge-strip--black { left: 0; top: 0; height: 158px; background: var(--ink-black); }
  .card--contact .edge-strip--green { left: 0; top: 158px; bottom: 0; background: var(--brand-green); }

  .holder-name {
    position: absolute; left: 58px; top: 118px;
    color: var(--brand-green); font-weight: 700; font-size: 23px; letter-spacing: 0.5px;
  }
  .contact-list {
    position: absolute; left: 58px; top: 190px;
    list-style: none; color: var(--text-light); font-size: 17px; line-height: 24px;
  }

  .wordmark {
    display: flex; align-items: center; gap: 10px;
    color: var(--brand-green); font-weight: 700; text-transform: uppercase;
    line-height: 1.05;
  }
  .wordmark__mark { background: var(--brand-green); flex: none; }
  .card--contact .wordmark { position: absolute; right: 40px; top: 42px; font-size: 25px; }
  .card--contact .wordmark__mark { width: 26px; height: 26px; }

  /* brand side */
  .card--brand .edge-strip--black { right: 0; top: 0; height: 180px; background: var(--ink-black); }
  .card--brand .edge-strip--green { right: 0; top: 180px; bottom: 0; background: var(--brand-green); }
  .card--brand .wordmark {
    position: absolute; left: 0; right: 0; top: 110px; justify-content: center;
    font-size: 46px;
  }
  .card--brand .wordmark__mark { width: 40px; height: 40px; }
  .website {
    position: absolute; left: 0; right: 0; top: 300px; text-align: center;
    font-weight: 700; font-size: 21px; color: var(--ink-black);
  }
  .website__domain { color: var(--brand-green); }
</style>
</head>
<body>
<main class="canvas">

  <section class="card card--contact" aria-label="Business card, contact side">
    <div class="edge-strip edge-strip--black"></div>
    <div class="contact-band"></div>
    <div class="edge-strip edge-strip--green"></div>

    <div class="wordmark">
      <span class="wordmark__mark" aria-hidden="true"></span>
      <span class="wordmark__name">Bright Parcel Route</span>
    </div>

    <h1 class="holder-name">GLEN HARWICK</h1>

    <ul class="contact-list">
      <li>Mobile: 917-555-4862</li>
      <li>Office: 516-555-7104</li>
      <li>Fax: 866-555-3927</li>
      <li>Email: info@brightparcelroute.example</li>
    </ul>
  </section>

  <section class="card card--brand" aria-label="Business card, brand side">
    <div class="edge-strip edge-strip--black"></div>
    <div class="edge-strip edge-strip--green"></div>

    <div class="wordmark">
      <span class="wordmark__mark" aria-hidden="true"></span>
      <span class="wordmark__name">Bright Parcel Route</span>
    </div>

    <p class="website">www.<span class="website__domain">brightparcelroute</span>.example</p>
  </section>

</main>
</body>
</html>
```